T.B.W.L. Business Card Design

we need a business card design for a motor vehicle repair business in Southport Australia, called Trevan's Automotive Repair Services. Our services include panel & paint, resprays and light bodyworks. We have a logo which we would like to use on the business card. We would like to see designs that use the colours blue and grey.

Industry/Entity Type

Automotive

Contact Information for Business Card

Trevan's Automotive Repair Services,
Delwyn Orsk,
7/2-4 Quarrow Street Southport 4215, 0471 862 307, /trevansautomotiverepairservices, trevansautomotiverepairservices@examplemail.test,
services: panel & paint, respray, light bodyworks.
ABN: 47 612 098 254

Requirements
Must have
• Front of card must include attached logo and contact details.
please list services
Your eye should be drawn to the name (Delwyn Orsk) and phone number (0471 862 307).
Font must be legible and contemporary.
back of business card should have the following:
1. title - quote and
2. list the following: for, date, valid till, quote details and
3. a footer "to book you repair, please contact Delwyn Orsk on 0471 862 307".
There needs to be enough space to hand write details.
Should not have
• do not include any graphics/illustrations.

```html
<!DOCTYPE html>
<html lang="en">
<head>
<meta charset="utf-8">
<title>T.B.W.L. Business Card Design</title>
<link href="https://fonts.googleapis.com/css2?family=Lato:wght@400;700;900&display=swap" rel="stylesheet">
<style>
  :root {
    --brand-blue: #1a86c8;
    --brand-blue-dark: #1570a8;
    --ink: #111111;
    --band-black: #0b0b0b;
    --paper: #ffffff;
    --rule-grey: #9a9a9a;
    --backdrop: #5a5d61;
  }
  * { box-sizing: border-box; margin: 0; padding: 0; }
  html, body {
    width: 1200px; height: 926px; overflow: hidden;
    background: var(--backdrop);
    font-family: "Lato", Arial, sans-serif;
  }
  .canvas {
    position: relative; width: 1200px; height: 926px;
    display: flex; flex-direction: column; align-items: center; justify-content: center; gap: 40px;
  }
  .card {
    position: relative; width: 660px; height: 404px; overflow: hidden;
    box-shadow: 0 8px 24px rgba(0,0,0,.35);
  }

  /* Front */
  .card-front { background: var(--paper); }
  .front-top { position: absolute; left: 0; top: 0; width: 100%; height: 232px; }
  .brand-mark {
    position: absolute; left: 34px; top: 78px; width: 250px;
    display: flex; align-items: center; gap: 12px;
  }
  .brand-dot { flex: none; width: 18px; height: 18px; border-radius: 50%; background: var(--brand-blue); }
  .brand-name {
    font-weight: 900; color: var(--brand-blue-dark); font-size: 20px; line-height: 1.15; text-transform: uppercase;
  }
  .divider { position: absolute; left: 300px; top: 40px; width: 1px; height: 160px; background: var(--rule-grey); }
  .contact { position: absolute; left: 322px; top: 52px; }
  .person-name { font-size: 36px; color: var(--brand-blue); font-weight: 400; letter-spacing: .5px; line-height: 1; }
  .person-name strong { font-weight: 700; }
  .contact-list { list-style: none; margin-top: 14px; font-weight: 700; color: var(--ink); font-size: 17px; line-height: 1.35; }
  .contact-list .label { color: var(--brand-blue); }
  .contact-list .email { font-weight: 400; font-size: 12.5px; }
  .address-band {
    position: absolute; left: 0; top: 232px; width: 100%; height: 34px; background: var(--band-black);
    color: var(--paper); font-size: 15px; display: flex; align-items: center; justify-content: center; letter-spacing: .3px;
  }
  .services {
    position: absolute; left: 0; top: 266px; width: 100%; height: 138px; background: var(--brand-blue);
    color: var(--paper); text-align: center; padding-top: 28px;
  }
  .services-title { font-size: 24px; font-weight: 900; letter-spacing: 1px; }
  .services-list { margin-top: 14px; font-size: 18px; font-weight: 700; letter-spacing: 4px; }

  /* Back */
  .card-back { background: var(--brand-blue); color: var(--paper); }
  .back-brand {
    position: absolute; left: 0; top: 26px; width: 100%;
    display: flex; justify-content: center; align-items: center; gap: 10px;
  }
  .back-brand .brand-dot { background: var(--paper); width: 14px; height: 14px; }
  .back-brand .brand-name { color: var(--paper); font-size: 16px; text-align: center; }
  .quote-box {
    position: absolute; left: 44px; top: 90px; width: 572px; height: 196px; background: var(--paper);
    color: var(--ink); padding: 20px 26px; font-size: 14px; text-transform: uppercase;
  }
  .quote-row { display: flex; align-items: flex-end; gap: 8px; height: 30px; }
  .fill-line { flex: 1; border-bottom: 1px solid var(--ink); height: 1px; margin-bottom: 4px; }
  .blank-line { border-bottom: 1px solid var(--ink); height: 34px; }
  .booking { position: absolute; left: 0; top: 308px; width: 100%; text-align: center; font-size: 18px; line-height: 1.35; }
  .booking-title { text-transform: uppercase; }
  .booking strong { font-weight: 900; }
</style>
</head>
<body>
<main class="canvas">
  <section class="card card-front" aria-label="Business card front">
    <div class="front-top">
      <div class="brand-mark">
        <span class="brand-dot"></span>
        <span class="brand-name">Trevan's Automotive Repair Services</span>
      </div>
      <div class="divider"></div>
      <div class="contact">
        <h1 class="person-name">DELWYN <strong>ORSK</strong></h1>
        <ul class="contact-list">
          <li><span class="label">P:</span> 0471 862 307</li>
          <li><span class="label">ABN:</span> 47 612 098 254</li>
          <li class="email"><span class="label">E:</span> trevansautomotiverepairservices@examplemail.test</li>
        </ul>
      </div>
    </div>
    <div class="address-band">Trevan's Automotive Repair Services,&nbsp; 7/2-4 Quarrow Street Southport 4215</div>
    <div class="services">
      <h2 class="services-title">SERVICES</h2>
      <p class="services-list">PANEL &amp; PAINT, RESPRAY, LIGHT BODYWORKS</p>
    </div>
  </section>

  <section class="card card-back" aria-label="Business card back">
    <div class="back-brand">
      <span class="brand-dot"></span>
      <span class="brand-name">Trevan's Automotive<br>Repair Services</span>
    </div>
    <div class="quote-box">
      <div class="quote-row"><span>Date</span><span class="fill-line"></span></div>
      <div class="quote-row"><span>Quote details</span><span class="fill-line"></span><span>Valid till</span><span class="fill-line"></span></div>
      <div class="blank-line"></div>
      <div class="blank-line"></div>
      <div class="blank-line"></div>
    </div>
    <div class="booking">
      <p class="booking-title">To book you repair</p>
      <p>Please contact <strong>Delwyn Orsk</strong> on <strong>0471 862 307</strong></p>
    </div>
  </section>
</main>
</body>
</html>
```